Accountants Stationary Package

Letter head, compliment slip, business card, report cover

Using selected logo which will be supplied when available design with compliment slip, letter head, business card and report cover. Some information to be amended and will be supplied at revision stage, design needs to resonate with chosen logo.
Updates

Update information 1 business card - my name is "Martin Keeley" post numerals are FCA , TITLE = Managing Director, (but maybe chartered accountant) is ok, my personal mobile is 0417 55 58 66 and personal email ids martin.k@keeleyledger.com,au, I like the tag line included " everybody ....succcess" Don't want professional liability logo but ok with the PQ and tallo logo I like the colours I like the blue back where it has a soft watermark finish 2. letterheads Need logos for tallo, PQ, professional standards Needs full company name and ABN NUMmber as - Keeley Accounting Pty Limited, ACN 748 301 526 Linked in ? I am also ok with initials instead of icons for phone, email, fax mobile, etc

Industry/Entity Type

Accounting

Requirements
Must have
• Keeley Accounting Pty Limited
• ABN 456456456
• Charted accountants
• Telephone 612 48559302
• Fax 612 4857 1438
• Po Box 5864, Erina, NSW, 2250
• Mobile 0417 555 866
• Address 42 Wendover road, Erina, suite 3 Wendover Hub
• Mail@keeleyledger.com.au
• Website keeleyledger.com.au
• List of services;
• Tax and Accounting
• Business Development
• Superannuation and Financial Services

```html
<!DOCTYPE html>
<html lang="en">
<head>
<meta charset="utf-8">
<title>Keeley Accounting – Stationery Package</title>
<link rel="stylesheet" href="https://fonts.googleapis.com/css2?family=Open+Sans:wght@400;600;700&family=Arimo:wght@400&family=Great+Vibes&display=swap">
<style>
  :root {
    --stage: #c8c8c8;
    --paper: #ffffff;
    --brand-blue: #29a8df;
    --brand-blue-soft: #4cb8e6;
    --brand-orange: #f15a24;
    --ink: #333333;
    --ink-soft: #555555;
    --badge-grey: #9aa3ad;
    --white: #ffffff;
  }
  * { box-sizing: border-box; margin: 0; padding: 0; }
  html, body { width: 1200px; height: 562px; overflow: hidden; background: var(--stage); }
  body { position: relative; font-family: "Open Sans", Arial, sans-serif; color: var(--ink); }

  .sheet { position: absolute; background: var(--paper); box-shadow: 0 1px 3px rgba(0,0,0,.25); overflow: hidden; }
  .caption { position: absolute; font-size: 7px; color: var(--ink); text-align: center; }

  .brand { position: absolute; display: flex; align-items: center; gap: 4px; }
  .brand-square { background: var(--brand-blue); display: block; }
  .brand-name { font-weight: 700; color: var(--brand-blue); letter-spacing: .02em; line-height: 1; }

  .badges { position: absolute; display: flex; align-items: center; gap: 6px; }
  .badge-square { background: var(--badge-grey); display: block; }
  .badge-circle { background: var(--brand-blue); border-radius: 50%; display: block; }

  .band { position: absolute; left: 0; right: 0; height: 9px; background: var(--brand-blue); color: var(--white);
          font-size: 5px; letter-spacing: .14em; display: flex; align-items: center; justify-content: center; }
  .band-end { position: absolute; right: 0; top: 0; bottom: 0; background: var(--brand-orange); }

  /* letter */
  .letter { left: 50px; top: 48px; width: 340px; height: 478px; }
  .letter .salutation { position: absolute; left: 26px; top: 116px; font-family: "Arimo", Arial, sans-serif; font-size: 10px; }
  .letter .body { position: absolute; left: 26px; top: 142px; width: 292px; font-family: "Arimo", Arial, sans-serif;
                  font-size: 5.2px; line-height: 8.4px; color: var(--ink-soft); text-align: justify; }
  .letter .body p { margin-bottom: 8px; }
  .letter .signoff { position: absolute; left: 26px; top: 336px; font-family: "Arimo", Arial, sans-serif; font-size: 5.4px; }
  .letter .signature { position: absolute; left: 26px; top: 346px; width: 48px; height: 18px;
                       background: linear-gradient(90deg, #e6e6e6, #f4f4f4); border-radius: 2px; }
  .letter .signer { position: absolute; left: 26px; top: 374px; font-family: "Arimo", Arial, sans-serif; font-size: 7.5px; }
  .letter .signer small { display: block; font-size: 5.2px; margin-top: 2px; }
  .letter .footer { position: absolute; left: 0; right: 0; top: 434px; text-align: center; font-size: 5.4px; line-height: 9px; }
  .label { color: var(--brand-blue); font-weight: 700; }

  /* business card */
  .card { width: 186px; height: 106px; }
  .card-front { left: 513px; top: 90px; }
  .card-front .person { position: absolute; left: 8px; top: 55px; width: 94px; text-align: center; }
  .card-front .person strong { display: block; font-size: 7px; color: var(--brand-blue); font-weight: 600; }
  .card-front .person span { display: block; font-size: 4.6px; color: var(--brand-orange); font-weight: 600; }
  .card-front .divider { position: absolute; left: 106px; top: 18px; width: 0.6px; height: 62px; background: #bbb; }
  .card-front .contact { position: absolute; left: 111px; top: 18px; font-size: 4.4px; line-height: 6.6px; white-space: nowrap; }
  .card-front .contact .gap { display: block; height: 3px; }

  .card-back { top: 218px; background: var(--brand-blue); color: var(--white); text-align: center; }
  .card-back-one { left: 414px; }
  .card-back-two { left: 608px; }
  .backdrop { position: absolute; inset: 0; }
  .card-back-one .backdrop { background: linear-gradient(135deg, var(--brand-blue-soft), var(--brand-blue)); }
  .card-back-two .backdrop { background: linear-gradient(110deg, var(--brand-blue-soft) 0%, var(--brand-blue) 55%); }
  .card-back .panel { position: absolute; top: 22px; width: 96px; }
  .card-back-one .panel { left: 45px; }
  .card-back-two .panel { right: 6px; }
  .card-back .badges { position: static; justify-content: center; }
  .card-back .badge-square, .card-back .badge-circle { background: var(--white); }
  .card-back .rule { height: 0.5px; background: rgba(255,255,255,.8); margin: 6px 0 4px; }
  .card-back .services { font-size: 4.3px; line-height: 6px; }
  .card-back .tagline { font-size: 4.6px; font-weight: 400; letter-spacing: .04em; }

  /* compliment slip */
  .slip { left: 414px; top: 350px; width: 381px; height: 174px; }
  .slip .address { position: absolute; left: 19px; top: 113px; font-size: 5.5px; line-height: 8px; white-space: nowrap; }
  .slip .greeting { position: absolute; left: 200px; top: 112px; font-family: "Great Vibes", cursive;
                    font-size: 22px; color: var(--brand-blue); }

  /* report cover */
  .cover { left: 818px; top: 48px; width: 323px; height: 478px; background: var(--brand-blue); }
  .cover .brand { left: 68px; top: 212px; gap: 14px; }
  .cover .brand-square { background: var(--white); }
  .cover .brand-name { color: var(--white); }
</style>
</head>
<body>

<section class="sheet letter" aria-label="Letterhead">
  <div class="brand" style="left:26px;top:26px;">
    <span class="brand-square" style="width:18px;height:18px;"></span>
    <span class="brand-name" style="font-size:13px;">KEELEY</span>
  </div>
  <div class="badges" style="left:266px;top:28px;">
    <span class="badge-square" style="width:16px;height:16px;"></span>
    <span class="badge-circle" style="width:17px;height:17px;"></span>
  </div>

  <p class="salutation">Dear Mr. Smith,</p>
  <div class="body">
    <p>Lorem ipsum dolor sit amet, consectetur adipiscing elit. Donec orci purus, luctus vitae dignissim eu, iaculis sed purus. Vivamus faucibus, ipsum nec aliquet viverra, leo mauris condimentum ligula, sit amet sagittis enim ligula quis arcu. Nam egestas tortor id nisi porttitor mattis. In tortor ante, ultricies in suscipit a, tempus non massa. Vivamus et auctor mi. Fusce vel massa nulla. Phasellus nec eros mauris, et scelerisque orci.</p>
    <p>Donec malesuada orci vitae nulla accumsan porta a id massa. Quisque accumsan iaculis magna sit amet fringilla. Maecenas consequat, magna eget tincidunt semper, odio nibh rutrum mi, id feugiat ante nisi eu risus. Vestibulum nunc orci, rhoncus a placerat in, ultricies in mi. Cras mattis varius eros, vel fringilla nisi suscipit eget. Quisque scelerisque sagittis nulla at porttitor.</p>
    <p>Sed id augue vitae urna euismod commodo aliquet a quam. Pellentesque arcu velit, cursus et malesuada ut, consequat et diam. Nullam erat sem, rhoncus id ullamcorper vitae, rhoncus et arcu. In ultricies ultricies nulla, ut rutrum nisi iaculis at. Donec eu magna a metus ornare faucibus. Fusce aliquet faucibus ultricies. Morbi semper, est id tincidunt gravida, sem arcu adipiscing lacus, ac bibendum nulla leo eu purus. Quisque nec diam sed risus consectetur a ccumsan quis quis nibh. Vestibulum id purus lorem.</p>
    <p>It is a long established fact that a reader will be distracted by the readable content of a page when looking at its layout. The point of using Lorem Ipsum is that it has a more-or-less normal distribution of letters, as opposed to using 'Content here, content here', making it look like readable English. Many desktop publishing packages</p>
  </div>
  <p class="signoff">Sincerely,</p>
  <div class="signature" role="img" aria-label="Handwritten signature"></div>
  <p class="signer">Martin Keeley, FCA<small>Managing Director</small></p>
  <div class="footer">
    Po Box 5864, Halden Vale, NSW, 2299 | 42 Wendover road, Halden Vale, suite 3 Wendover Hub<br>
    <span class="label">T:</span> 612 48559302 <span class="label">C:</span> 0417 55 58 66 <span class="label">F:</span> 612 4857 1438 <span class="label">E:</span>martin.k@keeleyledger.com,au <span class="label">IN:</span>keeleyledger
  </div>
  <div class="band" style="top:458px;">www.keeleyledger.com.au<span class="band-end" style="width:42px;"></span></div>
</section>
<p class="caption" style="left:180px;top:534px;width:80px;">Letter</p>

<section class="sheet card card-front" aria-label="Business card front">
  <div class="brand" style="left:14px;top:34px;">
    <span class="brand-square" style="width:15px;height:15px;"></span>
    <span class="brand-name" style="font-size:11px;">KEELEY</span>
  </div>
  <div class="person"><strong>Martin Keeley, FCA</strong><span>Managing Director</span></div>
  <div class="divider"></div>
  <div class="contact">
    Po Box 5864, Halden Vale, NSW, 2299<br>42 Wendover road, Halden Vale<br>suite 3 Wendover Hub<span class="gap"></span>
    <span class="label">T :</span> 612 48559302<br>
    <span class="label">C :</span> 0417 55 58 66<br>
    <span class="label">F :</span> 612 4857 1438<br>
    <span class="label">E :</span> martin.k@keeleyledger.com,au<br>
    <span class="label">In :</span> /keeleyledger
  </div>
  <div class="band" style="top:92px;">www.keeleyledger.com.au<span class="band-end" style="width:22px;"></span></div>
</section>
<p class="caption" style="left:566px;top:201px;width:80px;">Front</p>

<section class="sheet card card-back card-back-one" aria-label="Business card back, version one">
  <div class="backdrop" role="img" aria-label="Soft blue watermark pattern"></div>
  <div class="panel">
    <div class="badges">
      <span class="badge-square" style="width:18px;height:18px;"></span>
      <span class="badge-circle" style="width:26px;height:26px;"></span>
    </div>
    <div class="rule"></div>
    <p class="services">Tax &amp; Accounting • Business Development<br>Superannuation &amp; Financial Services</p>
    <div class="rule"></div>
    <p class="tagline">EVERYBODY .... SUCCCESS</p>
  </div>
</section>
<p class="caption" style="left:467px;top:330px;width:80px;">Back 01</p>

<section class="sheet card card-back card-back-two" aria-label="Business card back, version two">
  <div class="backdrop" role="img" aria-label="Large faint brand watermark"></div>
  <div class="panel">
    <div class="badges">
      <span class="badge-square" style="width:16px;height:16px;"></span>
      <span class="badge-circle" style="width:22px;height:22px;"></span>
    </div>
    <div class="rule"></div>
    <p class="services">Tax &amp; Accounting • Business Development<br>Superannuation &amp; Financial Services</p>
    <div class="rule"></div>
    <p class="tagline">EVERYBODY .... SUCCCESS</p>
  </div>
</section>
<p class="caption" style="left:661px;top:330px;width:80px;">Back 02</p>

<section class="sheet slip" aria-label="Compliment slip">
  <div class="brand" style="left:24px;top:20px;">
    <span class="brand-square" style="width:18px;height:18px;"></span>
    <span class="brand-name" style="font-size:13px;">KEELEY</span>
  </div>
  <div class="badges" style="left:318px;top:22px;">
    <span class="badge-square" style="width:15px;height:15px;"></span>
    <span class="badge-circle" style="width:16px;height:16px;"></span>
  </div>
  <div class="address">
    Po Box 5864, Halden Vale, NSW, 2299<br>
    42 Wendover road, Halden Vale, suite 3 Wendover Hub<br>
    <span class="label">T:</span> 612 48559302 <span class="label">C:</span> 0417 55 58 66 <span class="label">F:</span> 612 4857 1438<br>
    <span class="label">E:</span>martin.k@keeleyledger.com,au <span class="label">IN:</span>keeleyledger
  </div>
  <p class="greeting">With Compliments</p>
  <div class="band" style="top:157px;">www.keeleyledger.com.au<span class="band-end" style="width:42px;"></span></div>
</section>
<p class="caption" style="left:564px;top:534px;width:80px;">Compliments</p>

<section class="sheet cover" aria-label="Report cover">
  <div class="brand">
    <span class="brand-square" style="width:50px;height:50px;"></span>
    <span class="brand-name" style="font-size:34px;">KEELEY</span>
  </div>
</section>
<p class="caption" style="left:939px;top:534px;width:80px;">Report Cover</p>

</body>
</html>
```